Bill board design For Marlowe’s Construction

Billboard Design Request
Please design the billboard to match the branding, colors, and overall feel of our website: Marlowe's Construction Website
MARLOWE’S CONSTRUCTION
CONCRETE BUILT FOR GENERATIONS
⭐ 5-Star Rated on Zorvix
Please Include:
* All three attached project photos
* Company logo(s)
* Phone Number: 555-214-7630
* Website: MarlowesConstruction.example
* Zorvix logo with 5-star rating graphic
* Chatterly logo
* Pixtoria logo
Service Area:
Kalamazoo • Battle Creek • Coldwater • Grand Rapids
Please arrange the photos and layout in whatever way creates the strongest visual impact and readability from the road. The company name, headline, phone number, and website should be highly visible at highway speeds.
The overall appearance should be clean, professional, premium, and consistent with our website branding while highlighting our reputation, craftsmanship, and quality concrete work.
People Driving By
Concrete Construction

```html
<!DOCTYPE html>
<html lang="en">
<head>
<meta charset="utf-8">
<title>Marlowe’s Construction Billboard</title>
<link rel="stylesheet" href="https://fonts.googleapis.com/css2?family=Krona+One&family=Montserrat:wght@600;800&family=Oswald:wght@500;600&display=swap">
<style>
  :root {
    --page: #e9ecef;
    --board: #232323;
    --blue: #1e82e0;
    --white: #ffffff;
    --ink: #151515;
    --gray: #8a8a8a;
  }
  * { box-sizing: border-box; margin: 0; padding: 0; }
  html, body { width: 1200px; height: 1029px; overflow: hidden; background: var(--page); }
  .billboard {
    position: absolute; left: 20px; top: 224px; width: 1160px; height: 580px;
    background: var(--board); overflow: hidden;
  }
  .brand {
    position: absolute; left: 150px; top: 62px; text-align: center;
    font-family: "Montserrat", sans-serif;
  }
  .brand-name { color: var(--blue); font-weight: 800; font-size: 30px; letter-spacing: 0.5px; }
  .brand-sub { color: var(--gray); font-weight: 600; font-size: 11px; letter-spacing: 5px; margin-top: 2px; }
  .headline {
    position: absolute; left: 430px; top: 48px;
    font-family: "Krona One", sans-serif; font-size: 40px; line-height: 1.2; font-weight: 400;
  }
  .headline .line-1 { color: var(--blue); }
  .headline .line-2 { color: var(--white); }
  .projects { position: absolute; left: 0; top: 178px; width: 1160px; height: 220px; }
  .project {
    position: absolute; top: 0; height: 220px; width: 345px;
    clip-path: polygon(18% 0, 100% 0, 82% 100%, 0 100%);
  }
  .project-edge {
    position: absolute; top: 4px; height: 220px; width: 345px; background: var(--blue);
    clip-path: polygon(18% 0, 100% 0, 82% 100%, 0 100%);
  }
  .edge-1 { left: 42px; }
  .edge-2 { left: 409px; }
  .edge-3 { left: 776px; }
  .project-1 { left: 38px; background: linear-gradient(160deg, #9aa08a, #5b4a3a 55%, #2a2724); }
  .project-2 { left: 405px; background: linear-gradient(180deg, #7e8a6a, #6f5f6a 45%, #c9c2b8); }
  .project-3 { left: 772px; background: linear-gradient(180deg, #8a6b58, #5b6a42 50%, #b8643a); }
  .service {
    position: absolute; left: 140px; top: 418px; display: flex; align-items: baseline; gap: 48px;
    font-family: "Oswald", sans-serif; font-weight: 600; font-size: 26px; letter-spacing: 1.5px;
    white-space: nowrap;
  }
  .service-label { color: var(--blue); }
  .service-cities { color: var(--white); display: flex; gap: 14px; align-items: baseline; }
  .service-cities .dot { color: var(--blue); }
  .call-band {
    position: absolute; left: 0; top: 466px; width: 480px; height: 114px; background: var(--blue);
    clip-path: polygon(0 0, 100% 0, 90% 100%, 0 100%);
    display: flex; align-items: center; gap: 16px; padding-left: 28px;
  }
  .call-icon { width: 40px; height: 40px; flex: none; }
  .call-number { font-family: "Montserrat", sans-serif; font-weight: 800; font-size: 40px; color: var(--white); white-space: nowrap; }
  .info-band {
    position: absolute; left: 430px; top: 492px; width: 730px; height: 88px; background: var(--white);
    clip-path: polygon(5% 0, 100% 0, 100% 100%, 0 100%);
    display: flex; align-items: center; justify-content: space-between;
    padding-left: 62px; padding-right: 22px;
    font-family: "Oswald", sans-serif; color: var(--ink); white-space: nowrap;
  }
  .reviews { display: flex; flex-direction: column; align-items: center; line-height: 1.1; }
  .reviews-name { font-size: 22px; font-weight: 600; }
  .reviews-stars { display: flex; gap: 3px; align-items: center; font-size: 11px; font-weight: 500; }
  .social { display: flex; align-items: center; gap: 6px; font-size: 15px; font-weight: 500; }
  .social-dot { width: 14px; height: 14px; border-radius: 50%; background: var(--blue); flex: none; }
  .website { display: flex; align-items: center; gap: 8px; font-size: 21px; font-weight: 600; }
  .website-icon { width: 24px; height: 24px; flex: none; }
</style>
</head>
<body>
  <main class="billboard">
    <div class="brand">
      <div class="brand-name">MARLOWE’S</div>
      <div class="brand-sub">CONSTRUCTION L.L.C</div>
    </div>

    <h1 class="headline">
      <div class="line-1">CONCRETE BUILT</div>
      <div class="line-2">FOR GENERATIONS</div>
    </h1>

    <section class="projects">
      <div class="project-edge edge-1"></div>
      <div class="project project-1" role="img" aria-label="Crew pouring and spreading fresh concrete on a residential job"></div>
      <div class="project-edge edge-2"></div>
      <div class="project project-2" role="img" aria-label="Brick detached garage with a new smooth concrete driveway"></div>
      <div class="project-edge edge-3"></div>
      <div class="project project-3" role="img" aria-label="Stamped terracotta-toned concrete walkway leading to a house"></div>
    </section>

    <div class="service">
      <span class="service-label">SERVICE AREA:</span>
      <span class="service-cities">
        <span>KALAMAZOO</span><span class="dot">•</span>
        <span>BATTLE CREEK</span><span class="dot">•</span>
        <span>COLDWATER</span><span class="dot">•</span>
        <span>GRAND RAPIDS</span>
      </span>
    </div>

    <div class="call-band">
      <svg class="call-icon" viewBox="0 0 40 40" aria-hidden="true">
        <circle cx="20" cy="20" r="19" fill="#fff"/>
        <path d="M14 10c1-.5 2 0 2.5 1l1.8 3.6c.4.9.1 1.8-.6 2.3l-1.3 1c1 2.3 2.8 4.2 5 5.3l1-1.3c.6-.7 1.5-1 2.3-.6l3.6 1.8c1 .5 1.4 1.6 1 2.5l-1 2.2c-.6 1.2-2 1.9-3.3 1.6C17.8 27.8 12.4 22.3 10.6 15.1c-.3-1.3.4-2.7 1.6-3.3z" fill="#1e82e0"/>
      </svg>
      <span class="call-number">555-214-7630</span>
    </div>

    <div class="info-band">
      <div class="reviews">
        <span class="reviews-name">Zorvix</span>
        <span class="reviews-stars">Reviews
          <svg width="62" height="11" viewBox="0 0 62 11" aria-hidden="true" fill="#f5b400">
            <polygon points="5.5,0 7,4 11,4 7.8,6.5 9,10.5 5.5,8 2,10.5 3.2,6.5 0,4 4,4"/>
            <polygon transform="translate(12.7 0)" points="5.5,0 7,4 11,4 7.8,6.5 9,10.5 5.5,8 2,10.5 3.2,6.5 0,4 4,4"/>
            <polygon transform="translate(25.4 0)" points="5.5,0 7,4 11,4 7.8,6.5 9,10.5 5.5,8 2,10.5 3.2,6.5 0,4 4,4"/>
            <polygon transform="translate(38.1 0)" points="5.5,0 7,4 11,4 7.8,6.5 9,10.5 5.5,8 2,10.5 3.2,6.5 0,4 4,4"/>
            <polygon transform="translate(50.8 0)" points="5.5,0 7,4 11,4 7.8,6.5 9,10.5 5.5,8 2,10.5 3.2,6.5 0,4 4,4"/>
          </svg>
        </span>
      </div>
      <div class="social"><span class="social-dot"></span>Chatterly</div>
      <div class="social"><span class="social-dot"></span>Pixtoria</div>
      <div class="website">
        <svg class="website-icon" viewBox="0 0 26 26" aria-hidden="true" fill="none" stroke="#1e82e0" stroke-width="2">
          <circle cx="13" cy="13" r="11"/>
          <ellipse cx="13" cy="13" rx="5" ry="11"/>
          <line x1="2" y1="13" x2="24" y2="13"/>
          <path d="M4 7h18M4 19h18"/>
        </svg>
        MARLOWESCONSTRUCTION.EXAMPLE
      </div>
    </div>
  </main>
</body>
</html>
```